We need letterhead, Business Cards, and envelops designed. We have attached a design of our logo and a sample of letterhead idea that was started but never perfected, it is only an idea for the letterhead if you can design something better we may love that also we are open to change.
We want a design that looks professional in style. we are a non profit trade association in the construction industry. the green color in the attached design represent green building, and we like that. also if you just want to enhance the letterhead sample that we attached that would be fine also.
Thanks and good luck
also the name that should show on the first business cards should be Merwin Habsfield, Director are web address is www.tqvmp.org

```html
<!DOCTYPE html>
<html lang="en">
<head>
<meta charset="utf-8">
<title>TQVMP Stationery Set</title>
<link rel="stylesheet" href="https://fonts.googleapis.com/css2?family=Open+Sans:wght@400;600;700&display=swap">
<style>
  :root {
    --bg: #e4e4e2;
    --paper: #ffffff;
    --paper-shade: #f1f1f0;
    --green: #8cc63f;
    --green-dark: #2f7d3a;
    --ink: #2b2b2b;
    --ink-soft: #555555;
    --charcoal: #2d2d2d;
  }
  * { box-sizing: border-box; margin: 0; padding: 0; }
  html, body { width: 1200px; height: 800px; overflow: hidden; }
  body {
    background: var(--bg);
    font-family: "Open Sans", sans-serif;
    color: var(--ink);
    position: relative;
  }
  .sheet {
    position: absolute;
    background: var(--paper);
    box-shadow: 0 2px 6px rgba(0,0,0,0.18);
    overflow: hidden;
  }
  .brand {
    display: flex;
    align-items: center;
    gap: 6px;
    font-weight: 700;
    color: var(--ink);
    letter-spacing: 1px;
  }
  .brand-square { width: 0.55em; height: 0.55em; background: var(--green-dark); }

  /* Letterhead */
  .letterhead { left: 60px; top: 128px; width: 420px; height: 544px; }
  .letterhead .brand { position: absolute; left: 34px; top: 30px; font-size: 30px; }
  .letterhead .top-rule {
    position: absolute; left: 150px; right: 28px; top: 56px; height: 3px;
    background: linear-gradient(90deg, var(--green-dark), var(--green) 70%, rgba(140,198,63,0));
  }
  .letter-body {
    position: absolute; left: 40px; right: 34px; top: 92px;
    font-size: 7.4px; line-height: 1.45; color: var(--ink-soft);
  }
  .letter-body p { margin-bottom: 8px; }
  .letter-body .signer { font-weight: 600; color: var(--green-dark); margin-bottom: 0; }
  .letter-web {
    position: absolute; right: 30px; bottom: 66px;
    font-size: 7.5px; color: var(--green-dark);
  }
  .letterhead .bottom-rule {
    position: absolute; left: 34px; right: 28px; bottom: 58px; height: 2px;
    background: linear-gradient(90deg, var(--green-dark), var(--green));
  }
  .letter-footer {
    position: absolute; left: 40px; bottom: 18px;
    font-size: 6.5px; line-height: 1.5; color: var(--ink-soft); text-transform: uppercase;
  }

  /* Envelopes */
  .envelope { left: 530px; width: 610px; height: 250px; background: var(--paper-shade); }
  .envelope-front { top: 60px; }
  .envelope-back { top: 332px; }
  .envelope .green-band {
    position: absolute; left: 0; top: 0; bottom: 0; width: 140px; background: var(--green);
  }
  .envelope-front .brand {
    position: absolute; left: 18px; top: 42px; font-size: 26px;
    background: var(--paper); padding: 4px 10px; border-bottom: 2px solid var(--green-dark);
  }
  .envelope-front .return-address {
    position: absolute; left: 14px; top: 168px;
    font-size: 6.5px; line-height: 1.5; color: var(--paper);
  }
  .envelope-front .web-bar {
    position: absolute; left: 0; bottom: 0; width: 140px; height: 30px;
    background: var(--charcoal); color: var(--paper);
    font-size: 7px; padding: 10px 14px;
  }
  .envelope-back .flap { position: absolute; left: 0; top: 0; width: 610px; height: 130px; }
  .envelope-back .brand {
    position: absolute; left: 250px; top: 40px; font-size: 28px;
    border-bottom: 2px solid var(--green-dark); padding-bottom: 2px;
  }

  /* Business cards */
  .card { top: 606px; width: 290px; height: 166px; }
  .card-front { left: 530px; }
  .card-back { left: 850px; }
  .card .green-half { position: absolute; left: 0; top: 0; bottom: 0; width: 50%; background: var(--green); }
  .card-front .brand {
    position: absolute; left: 50%; top: 50%; transform: translate(-50%, -50%);
    font-size: 30px; background: var(--paper); padding: 2px 10px;
  }
  .card-back .details {
    position: absolute; left: 155px; right: 12px; top: 14px; text-align: right;
  }
  .card-back .brand { justify-content: flex-end; font-size: 22px; border-bottom: 2px solid var(--green-dark); padding-bottom: 2px; }
  .card-back .name { font-size: 13px; margin-top: 10px; color: var(--ink); }
  .card-back .position { font-size: 8px; font-weight: 600; color: var(--ink-soft); }
  .card-back .contact { font-size: 6.5px; line-height: 1.5; color: var(--ink-soft); margin-top: 12px; }
</style>
</head>
<body>

  <section class="sheet letterhead">
    <div class="brand"><span>TQVMP</span><span class="brand-square"></span></div>
    <div class="top-rule"></div>
    <div class="letter-body">
      <p>2140, Quarry Hill Road<br>Fresno, CA 93701</p>
      <p>January 20th, 2011</p>
      <p>Mr. Calloway<br>President, Calloway Learning Center<br>88 Linden Court<br>Albany, NY 12207</p>
      <p>Dear Mr. Calloway,</p>
      <p>In the first paragraph, one needs to give a brief introduction of oneself. One should also give reference to the purpose of the letter in brief. The second paragraph needs to give the details of the letter and its need. This paragraph is mostly longer than the others and plays the main role in the letter. Keep the sentences short and to the point. Avoid using complex words and sentences.</p>
      <p>The third and last paragraph is the conclusion of the letter and can be kept short.</p>
      <p>Sincerely,</p>
      <p>(this is where the signature of the writer will be placed)</p>
      <p class="signer">Alden Parrow</p>
      <p>Read more at lettersample.net/professional-letter-format</p>
    </div>
    <div class="letter-web">www.tqvmp.org</div>
    <div class="bottom-rule"></div>
    <div class="letter-footer">Sunday Service, 9:00 AM<br>Map &amp; Directions<br>(555) 204-7731</div>
  </section>

  <section class="sheet envelope envelope-front">
    <div class="green-band"></div>
    <div class="brand"><span>TQVMP</span><span class="brand-square"></span></div>
    <div class="return-address">2140 Quarry Hill Road<br>Fresno, CA 93701<br>(555) 204-7731</div>
    <div class="web-bar">www.tqvmp.org</div>
  </section>

  <section class="sheet envelope envelope-back">
    <div class="green-band"></div>
    <svg class="flap" viewBox="0 0 610 130" aria-hidden="true">
      <polygon points="0,0 610,0 610,20 330,128 0,40" fill="#ffffff"/>
      <polygon points="0,0 140,0 140,34 0,40" fill="#7fb834"/>
      <polyline points="0,40 330,128 610,20" fill="none" stroke="#d6d6d4" stroke-width="1.5"/>
    </svg>
    <div class="brand"><span>TQVMP</span><span class="brand-square"></span></div>
  </section>

  <section class="sheet card card-front">
    <div class="green-half"></div>
    <div class="brand"><span>TQVMP</span><span class="brand-square"></span></div>
  </section>

  <section class="sheet card card-back">
    <div class="green-half"></div>
    <div class="details">
      <div class="brand"><span>TQVMP</span><span class="brand-square"></span></div>
      <div class="name">Merwin Habsfield</div>
      <div class="position">Director</div>
      <div class="contact">2140 Quarry Hill Road<br>Fresno, CA 93701<br>(555) 204-7731<br>www.tqvmp.org</div>
    </div>
  </section>

</body>
</html>
```